Wordpress and Elementor Pro website

We need a Wordpress/Elementor Pro design for our website. We already have a logo design and installed Wordpress. We have some ideas concerning the design, and we will share two websites. Both the design and content placement we like about these websites. We would like to see designs that use the color Purple (the same as the logo color), white and black. We provide these services: SEO optimization, SEO copywriting and online campaigns. We will provide a list of the page's we would like to see in the design.

Target Market(s)

Entrepreneurs, business owners. Companies who would like to expand online with texts and SEO.

Industry/Entity Type

Digital Marketing

Coding

Coded - Design and coding required

Number of Pages Required

5+ page

Font styles to use
Sans Serif

Colors
886aae
fffefd
0355a3

Requirements
Must have
• Single pages and singel posts of Elementor so I can create new pages and blog posts in the future.

```html
<!DOCTYPE html>
<html lang="en">
<head>
<meta charset="utf-8">
<title>Veldmark Online</title>
<link href="https://fonts.googleapis.com/css2?family=Roboto:wght@300;400;500;700&display=swap" rel="stylesheet">
<style>
:root{
  --purple:#6a4bb2;
  --purple-dark:#4f2f9a;
  --purple-soft:#8c74c6;
  --ink:#1b1d3a;
  --text:#6f7280;
  --muted:#a7a9b4;
  --light:#f3f4f7;
  --white:#ffffff;
  --footer:#1d1e25;
  --line:#e4e5ea;
}
*{box-sizing:border-box;margin:0;padding:0}
html,body{width:1200px;height:2941px;overflow:hidden}
body{font-family:'Roboto',sans-serif;color:var(--ink);background:var(--white);position:relative}
.abs{position:absolute}
a{color:inherit;text-decoration:none}
.btn{position:absolute;background:var(--purple);color:#fff;font-size:11px;font-weight:500;border-radius:16px;display:flex;align-items:center;justify-content:center}

/* top bar */
.topbar{position:absolute;left:0;top:0;width:1200px;height:31px;background:var(--purple);color:#fff;font-size:10px}
.topbar span{position:absolute;top:10px;display:flex;align-items:center;gap:6px}
.topbar svg{width:9px;height:9px;fill:#fff}
.social{position:absolute;top:10px;right:222px;display:flex;gap:12px}
.social i{display:block;width:8px;height:8px;border-radius:2px;background:rgba(255,255,255,.85)}

/* hero */
.hero{position:absolute;left:0;top:31px;width:1200px;height:644px;background:linear-gradient(180deg,#5f6a78 0%,#4e5966 30%,#3d4652 70%,#2e353f 100%)}
.hero-shade{position:absolute;inset:0;background:linear-gradient(180deg,rgba(40,40,60,.25),rgba(30,30,45,.35))}
.brand{position:absolute;left:251px;top:40px;color:#fff;font-size:16px;font-weight:400;letter-spacing:1px;display:flex;align-items:center;gap:8px}
.brand b{display:block;width:12px;height:12px;border:1.5px solid #fff}
.perks{position:absolute;top:50px;left:642px;display:flex;color:#fff;font-size:10px;font-weight:500;line-height:12px}
.perk{display:flex;align-items:center;gap:10px;padding:0 18px;border-left:1px solid rgba(255,255,255,.3)}
.perk:first-child{border-left:none;padding-left:0}
.perk svg{width:17px;height:17px;stroke:#fff;fill:none;stroke-width:1.4}
.nav{position:absolute;left:234px;top:94px;width:731px;height:50px;background:#fff;display:flex;align-items:center;padding-left:18px;font-size:12px}
.nav a{margin-right:31px;position:relative;height:50px;line-height:50px}
.nav a.active:after{content:"";position:absolute;left:0;right:-18px;bottom:0;height:3px;background:var(--purple)}
.nav .quote{position:absolute;right:20px;top:11px;width:111px;height:29px;border-radius:15px;background:var(--purple);color:#fff;line-height:29px;text-align:center;font-size:10px;font-weight:500;margin:0}
.hero-label{position:absolute;top:273px;width:1200px;text-align:center;color:#fff;font-size:10px;font-weight:500}
.hero-title{position:absolute;top:290px;width:1200px;text-align:center;color:#fff;font-size:52px;font-weight:300;line-height:57px}
.hero-title strong{font-weight:700}

/* service cards */
.card{position:absolute;top:590px;width:231px;height:218px;background:#fff;border:1px solid var(--line);text-align:center}
.card.feature{background:linear-gradient(180deg,#7e66bd,#6c52b0);color:#fff;border:none}
.card .ico{width:48px;height:48px;border-radius:50%;background:var(--purple);margin:20px auto 0;display:flex;align-items:center;justify-content:center}
.card.feature .ico{background:#fff}
.card .ico svg{width:22px;height:22px;stroke:#fff;fill:none;stroke-width:1.5}
.card.feature .ico svg{stroke:var(--purple)}
.card h3{font-size:16px;font-weight:400;line-height:22px;margin-top:12px}
.card p{font-size:10px;color:var(--text);line-height:15px;margin-top:9px}
.card.feature p{color:#fff}
.card .more{display:block;font-size:10px;font-weight:500;color:var(--purple);margin-top:17px}
.card.feature .more{color:#fff}

/* about */
.vert-brand{position:absolute;left:60px;top:1205px;transform:rotate(-90deg);transform-origin:left top;color:var(--purple-soft);font-size:42px;font-weight:300;letter-spacing:4px;white-space:nowrap}
.about-label{position:absolute;left:235px;top:901px;font-size:10px;color:var(--muted);font-weight:500}
.about-title{position:absolute;left:235px;top:926px;font-size:30px;font-weight:300;line-height:32px}
.about-title strong{font-weight:700}
.about-lead{position:absolute;left:235px;top:1012px;width:320px;font-size:12.5px;line-height:19px;color:#3a3c52}
.about-body{position:absolute;left:235px;top:1090px;width:330px;font-size:10px;line-height:15.5px;color:var(--text)}
.mini{position:absolute;top:1166px;width:169px;height:55px;background:var(--light);display:flex;align-items:center;gap:10px;padding-left:16px;font-size:9.5px;color:var(--text);line-height:13px}
.mini .dot{width:28px;height:28px;border-radius:50%;background:var(--purple);display:flex;align-items:center;justify-content:center}
.mini.alt .dot{background:#fff;border:1.5px solid var(--purple-soft)}
.mini .dot svg{width:12px;height:12px;fill:#fff}
.mini.alt .dot svg{fill:none;stroke:var(--purple);stroke-width:2}
.mini u{color:var(--purple)}
.about-photo{position:absolute;left:609px;top:871px;width:356px;height:411px;background:linear-gradient(135deg,#c9d0d8 0%,#9aa4ae 45%,#4b5058 100%)}

/* customers */
.customers{position:absolute;left:0;top:1384px;width:1200px;height:291px;background:var(--light)}
.customers h2{position:absolute;top:52px;width:1200px;text-align:center;font-size:30px;font-weight:300}
.customers h2 strong{font-weight:700}
.logo-slot{position:absolute;top:160px;width:62px;height:62px;background:#8c8d92;opacity:.8}
.arrow{position:absolute;top:177px;width:20px;height:28px}
.arrow svg{width:20px;height:28px;stroke:var(--purple);stroke-width:4;fill:none}

/* values */
.values{position:absolute;left:0;top:1675px;width:1200px;height:486px;background:linear-gradient(180deg,#5838a6,#6547b0 60%,#7a62bc)}
.values .label{position:absolute;top:75px;width:1200px;text-align:center;color:#fff;font-size:10px;font-weight:500}
.values h2{position:absolute;top:97px;width:1200px;text-align:center;color:#fff;font-size:31px;font-weight:300;line-height:33px}
.values h2 strong{font-weight:700}
.vcard{position:absolute;top:218px;width:230px;height:170px;background:#fff;text-align:center;color:var(--ink)}
.vcard.feature{background:#5a36ad;color:#fff}
.vcard svg{width:28px;height:28px;margin-top:28px;fill:none;stroke:var(--purple);stroke-width:2}
.vcard.feature svg{stroke:#fff}
.vcard h4{font-size:14px;font-weight:500;line-height:15px;margin-top:8px}
.vcard p{font-size:10px;line-height:15px;margin-top:9px;padding:0 40px}

/* contact */
.contact-title{position:absolute;left:236px;top:2215px;font-size:30px;font-weight:300}
.contact-title strong{font-weight:700}
.contact-intro{position:absolute;left:236px;top:2258px;width:340px;font-size:10.5px;line-height:16px;color:#3a3c52}
.item{position:absolute;left:236px;width:335px;height:72px;border-bottom:1px solid var(--line)}
.item .circle{position:absolute;left:0;top:0;width:50px;height:50px;border-radius:50%;background:#c6bde0;display:flex;align-items:center;justify-content:center}
.item .circle svg{width:17px;height:17px;fill:var(--purple)}
.item h5{position:absolute;left:62px;top:4px;font-size:13px;font-weight:500}
.item p{position:absolute;left:62px;top:22px;font-size:10px;line-height:15px;color:var(--purple-soft)}
.item p b{color:var(--purple);font-weight:500}
.form{position:absolute;left:611px;top:2130px;width:356px;height:422px;background:#fff;box-shadow:0 4px 20px rgba(30,30,60,.12);text-align:center}
.form h3{font-size:15px;font-weight:500;margin-top:35px}
.form .sub{font-size:10.5px;line-height:16px;color:var(--text);margin-top:8px}
.field{position:absolute;height:27px;border:1px solid var(--line);background:#f7f7f9;font-size:10px;color:var(--text);text-align:left;padding:8px 9px}

/* footer */
.footer{position:absolute;left:0;top:2649px;width:1200px;height:292px;background:var(--footer);color:#fff}
.footer .fbrand{position:absolute;left:234px;top:48px;font-size:14px;letter-spacing:1px;display:flex;align-items:center;gap:7px}
.footer .fbrand b{width:10px;height:10px;border:1.5px solid #fff;display:block}
.footer .about{position:absolute;left:234px;top:88px;width:165px;font-size:9px;line-height:18.5px}
.footer .fsocial{position:absolute;left:234px;top:183px;display:flex;gap:14px}
.footer .fsocial i{width:8px;height:8px;background:#fff;border-radius:2px;display:block}
.footer h6{position:absolute;top:63px;font-size:11.5px;font-weight:500}
.footer ul{position:absolute;top:98px;list-style:none;font-size:9px;line-height:22px}
.footer .ci{position:absolute;left:608px;top:98px;font-size:9px;line-height:22px}
.footer .ci div{display:flex;align-items:center;gap:9px}
.footer .ci i{width:9px;height:9px;border-radius:50%;background:var(--purple-soft);display:block}
.footer .email{position:absolute;left:793px;top:92px;width:170px;height:27px;border-radius:14px;background:#3a3b44;font-size:9px;padding:8px 14px}
.footer .sub{position:absolute;left:794px;top:131px;width:105px;height:27px;border-radius:14px;border:1.5px solid var(--purple-soft);color:var(--purple-soft);font-size:10px;text-align:center;line-height:24px}
</style>
</head>
<body>

<div class="topbar">
  <span style="left:234px"><svg viewBox="0 0 10 10"><path d="M2 0l2 2-1 1.5c.5 1.3 1.3 2.1 2.5 2.5L7 5l2 2-1.2 2C4 9 1 6 1 1.2z"/></svg>(+1) 555-010-2040</span>
  <span style="left:358px"><svg viewBox="0 0 10 10"><path d="M0 2h10v6H0z"/></svg>hello@veldmark.example</span>
  <span style="left:493px"><svg viewBox="0 0 10 10"><path d="M5 0a3.5 3.5 0 013.5 3.5C8.5 6 5 10 5 10S1.5 6 1.5 3.5A3.5 3.5 0 015 0z"/></svg>18 Linden Lane, Netherlands</span>
  <span style="left:750px">Careers</span>
  <span style="left:797px">Help Desk</span>
  <div class="social"><i></i><i></i><i></i><i></i></div>
</div>

<div class="hero" role="img" aria-label="Photo of a young man working on a laptop on a leather sofa by a city-view window">
  <div class="hero-shade"></div>
</div>
<div class="brand"><b></b>VELDMARK</div>
<div class="perks">
  <div class="perk"><svg viewBox="0 0 18 18"><rect x="2" y="2" width="14" height="14" rx="2"/><path d="M5 9l3 3 5-6"/></svg>Good<br>Optimization</div>
  <div class="perk"><svg viewBox="0 0 18 18"><circle cx="9" cy="9" r="7"/><path d="M9 5v4l-2 2"/></svg>24/7<br>Service</div>
  <div class="perk" style="padding-left:22px"><svg viewBox="0 0 18 18"><path d="M3 8h3v8H3zM6 8l3-6c1.5 0 2 1 1.5 3H15l-1.5 9H6"/></svg>Qualified<br>Professionals</div>
</div>
<nav class="nav">
  <a class="active">Homepage</a><a>Services</a><a>Cases</a><a>About Us</a><a>Contact Us</a>
  <a class="quote">Get A Quote</a>
</nav>
<div class="hero-label">WE OFFER HIGHEST QUALITY WORK</div>
<h1 class="hero-title"><strong>Omdat online groeien</strong> in omzet<br>en winst een specialisme is</h1>
<a class="btn" style="left:543px;top:430px;width:114px;height:27px">About Us</a>

<div class="card" style="left:234px">
  <div class="ico"><svg viewBox="0 0 24 24"><circle cx="12" cy="12" r="4"/><path d="M12 3v3M12 18v3M3 12h3M18 12h3M5.6 5.6l2 2M16.4 16.4l2 2M5.6 18.4l2-2M16.4 7.6l2-2"/></svg></div>
  <h3>SEO<br>Optimization</h3>
  <p>Lorem ipsum dolor sit amet, consectet<br>adipiscing elit, sed do eius</p>
  <a class="more">Read More</a>
</div>
<div class="card feature" style="left:484px" role="img" aria-label="Service card over a purple-tinted photo of a woman using a laptop">
  <div class="ico"><svg viewBox="0 0 24 24"><circle cx="12" cy="12" r="2.5"/><path d="M12 3v6M12 15v6M3 12h6M15 12h6M6 6l4 4M14 14l4 4M6 18l4-4M14 10l4-4"/></svg></div>
  <h3>SEO<br>Copywriting</h3>
  <p>Lorem ipsum dolor sit amet, consectet<br>adipiscing elit, sed do eius</p>
  <a class="more">Read More</a>
</div>
<div class="card" style="left:733px">
  <div class="ico"><svg viewBox="0 0 24 24"><path d="M5 19v-3M9 19v-6M13 19v-8M17 19v-11M4 10l6-4 4 2 6-5"/></svg></div>
  <h3>Online<br>Campaigns</h3>
  <p>Lorem ipsum dolor sit amet, consectet<br>adipiscing elit, sed do eius</p>
  <a class="more">Read More</a>
</div>

<div class="vert-brand">VELDMARK</div>
<div class="about-label">ABOUT US</div>
<h2 class="about-title">Welcome to <strong>Veldmark<br>Online</strong></h2>
<p class="about-lead">Lorem ipsum dolor sit amet, consectetur adipiscing elit, sed do eiusmod tempor incididunt ut labore et dolore magna aliqua. Ut enim ad minim veniam.</p>
<p class="about-body">Lorem ipsum dolor sit amet, consectetur adipiscing elit, sed do eiusmod tempor incididunt ut labore et dolore magna aliqua. Ut enim ad minim veniam, quis nostrud exercitation ullamco Lorem ipsum dolor sit amet,</p>
<div class="mini" style="left:234px"><div class="dot"><svg viewBox="0 0 10 10"><path d="M2 0l2 2-1 1.5c.5 1.3 1.3 2.1 2.5 2.5L7 5l2 2-1.2 2C4 9 1 6 1 1.2z"/></svg></div><div>Contact Us<br><u>+1 555-010-2040</u></div></div>
<div class="mini alt" style="left:421px"><div class="dot"><svg viewBox="0 0 12 12"><circle cx="6" cy="6" r="5"/><path d="M6 3v3l2 1"/></svg></div><div>Our Email<br><u>hello@veldmark.example</u></div></div>
<a class="btn" style="left:234px;top:1251px;width:113px;height:29px">About Us</a>
<div class="about-photo" role="img" aria-label="Portrait photo of a man in glasses and a dark blazer in an office"></div>

<section class="customers">
  <h2>Our <strong>Customers</strong></h2>
  <div class="arrow" style="left:162px"><svg viewBox="0 0 20 28"><path d="M15 3L5 14l10 11"/></svg></div>
  <div class="logo-slot" style="left:231px;border-radius:50%"></div>
  <div class="logo-slot" style="left:367px"></div>
  <div class="logo-slot" style="left:503px;border-radius:50%"></div>
  <div class="logo-slot" style="left:641px"></div>
  <div class="logo-slot" style="left:771px;border-radius:50%"></div>
  <div class="logo-slot" style="left:902px"></div>
  <div class="arrow" style="left:1024px"><svg viewBox="0 0 20 28"><path d="M5 3l10 11L5 25"/></svg></div>
</section>

<section class="values" role="img" aria-label="Purple-tinted photo of a laptop and a glass on a desk">
  <div class="label">WELCOME TO VELDMARK</div>
  <h2>We understand the importance<br><strong>professionalism</strong></h2>
  <div class="vcard" style="left:235px"><svg viewBox="0 0 28 28"><circle cx="14" cy="12" r="7"/><path d="M7 12a7 7 0 0114 0M10 24h8"/></svg><h4>Customer<br>Care</h4><p>This area delivers the control you want over al critical aspects of your project.</p></div>
  <div class="vcard feature" style="left:485px"><svg viewBox="0 0 28 28"><circle cx="14" cy="14" r="10"/><circle cx="14" cy="14" r="5"/><path d="M14 2v24M2 14h24"/></svg><h4>Great<br>Results</h4><p>This area delivers the control you want over al critical aspects of your project.</p></div>
  <div class="vcard" style="left:734px"><svg viewBox="0 0 28 28"><path d="M14 4a8 8 0 00-8 8c0 4 3 6 3 10h10c0-4 3-6 3-10a8 8 0 00-8-8zM14 4v18"/></svg><h4>Years of<br>Experience</h4><p>This area delivers the control you want over al critical aspects of your project.</p></div>
</section>

<h2 class="contact-title">How to <strong>contact</strong> us</h2>
<p class="contact-intro">After we get some information from you, we'll set upa time to discuss y our project in further detail.</p>
<div class="item" style="top:2325px"><div class="circle"><svg viewBox="0 0 10 10"><path d="M5 0a3.5 3.5 0 013.5 3.5C8.5 6 5 10 5 10S1.5 6 1.5 3.5A3.5 3.5 0 015 0z"/></svg></div><h5>Our location</h5><p>42 Orchard Row, Netherlands<br><b>Find Us on Map</b></p></div>
<div class="item" style="top:2397px"><div class="circle"><svg viewBox="0 0 10 10"><path d="M2 0l2 2-1 1.5c.5 1.3 1.3 2.1 2.5 2.5L7 5l2 2-1.2 2C4 9 1 6 1 1.2z"/></svg></div><h5>Direct Line Numbers</h5><p>+1 555-014-3300<br>+1 555-014-3300</p></div>
<div class="item" style="top:2469px"><div class="circle"><svg viewBox="0 0 10 10"><path d="M0 2h10v6H0zM0 2l5 3.5L10 2" fill="none" stroke="#6a4bb2" stroke-width="1"/></svg></div><h5>Our Email</h5><p>sales@veldmark.example<br><b>hello@veldmark.example</b></p></div>

<form class="form">
  <h3>Let's Talk About Your Project</h3>
  <p class="sub">After we get some information from you, we'll set up<br>a time to discuss your project in further detail.</p>
  <div class="field" style="left:22px;top:114px;width:312px">Name</div>
  <div class="field" style="left:22px;top:155px;width:150px">Phone</div>
  <div class="field" style="left:184px;top:155px;width:150px">Email</div>
  <div class="field" style="left:22px;top:196px;width:312px">Subject</div>
  <div class="field" style="left:22px;top:237px;width:312px;height:93px">Message</div>
  <a class="btn" style="left:122px;top:356px;width:113px;height:27px">About Us</a>
</form>

<footer class="footer">
  <div class="fbrand"><b></b>VELDMARK</div>
  <p class="about">Lorem ipsum dolor sit amet, consectetur adipiscing elit, sed do eiusmod tempor incididunt ut labore et dolore magna aliqua. Ut enim ad minim veniam,</p>
  <div class="fsocial"><i></i><i></i><i></i><i></i></div>
  <h6 style="left:421px">Useful Links</h6>
  <ul style="left:421px"><li>Cases</li><li>About Us</li><li>Contact Us</li><li>Services</li></ul>
  <ul style="left:506px"><li>Cookie Policy</li><li>Exclaimer</li><li>Privacy Policy</li></ul>
  <h6 style="left:608px">Contacts</h6>
  <div class="ci">
    <div><i></i>Mon - Fri: 8.00am to 6.00pm</div>
    <div><i></i>7 Harbor Street, Netherlands</div>
    <div><i></i>+1 555-019-7788</div>
    <div><i></i>hello@veldmark.example</div>
  </div>
  <h6 style="left:795px">Newsletter</h6>
  <div class="email">Your email...</div>
  <div class="sub">Subscribe</div>
</footer>

</body>
</html>
```